Poster design for vitanest - Heal Your Hair

We need a poster to be made, Containing steps to heal hair along with the heading and other description. Please use good and free pics of hair from the net, attaching some related to every point.
Also need the Vitanest logo, website - [login to view URL] and the app download logos of playstore and app store. Attaching a sample poster with relevant files.
Please make it in a way that people share the poster with others on social media and put it on their desks or kitchen. (to be able to read them everyday)

Poster text starts -

Heal Your Hair

Keep your hair on and read on.

Reasons for hairfall
- Excess hairfall can mean that the body does not have enough reserves to address the needs of the hair.
- Underlying medical conditions like PCOD, thyroid problems and hormonal imbalances.
- Stress and no time for rest can cause premature greying and thinning of hair.
- A diet high in processed foods, sugar, refined grains, oils and animal products.
- Hard water & harsh chemicals in shampoos damage the hair shaft and follicle.
- Pollutants in air settle on the hair making it grimy, brittle and cause toxicity.
- Over treatment of hair with hair colourants, application of heat, tight braids and hair styling products damage the hair resulting in hairfall.

How can hairfall be reversed?
- Water rich fruits and vegetables in raw form, sprouts, nuts & seeds nourish the cells of the hair.
- Exercise to improve blood circulation and aid in toxin removal.
- Outdoor time to soak in sunlight and fresh air.
- Get good quality sleep everyday and adopt stress management techniques.
- Repair and growth happens best in a relaxed state.

Care of hair
- Use a soft bristled brush to distribute natural oil uniformly, dislodge dandruff and dirt.
- Massage your hair with your fingertips to stimulate good blood circulation.
- Bathe in lukewarm or cold water. Avoid using hot water as it reduces hair oils.
- Use coconut milk, fruit purees or reetha. Normal water is fine too.
- Dry your hair in sunlight as opposed to a hair dryer.
- Buy hair products which has more natural ingredients than chemicals.
- Shoulder & neck rotations improve circulation of nutrients to the hair follicles.

It may take time to see results. The hairfall you see today is the result of wrong lifestyle. Be patient and you will experience improvements in your crowning glory.

- Poster text ends.

please put relevant free pictures related to the topic and make the poster as attractive to the eye as possible.
Please put bullet points.
MAKE THE POSTER IN SUCH A WAY THAT PEOPLE WOULD WANT TO PUT IN THEIR KITCHEN , ROOMS OR SHARE WITH OTHERS.
- poster size - A3

```html
<!DOCTYPE html>
<html lang="en">
<head>
<meta charset="utf-8">
<title>Vitanest – Heal Your Hair</title>
<link rel="stylesheet" href="https://fonts.googleapis.com/css2?family=Roboto:wght@500;700;900&family=Roboto+Condensed:wght@400;500;700&display=swap">
<style>
  :root {
    --sky: #bfeef6;
    --mint: #dff5e6;
    --cream: #fbf3b8;
    --butter: #fbe7a0;
    --orange: #f0931e;
    --navy: #16295e;
    --brand-blue: #2b6fb3;
    --body-ink: #1f2a55;
    --green: #3f8a1e;
    --ink: #111111;
    --band: rgba(210, 240, 250, 0.85);
    --accent-blue: #4aa6e8;
  }
  * { box-sizing: border-box; margin: 0; padding: 0; }
  html, body { width: 854px; height: 1200px; overflow: hidden; }
  body {
    position: relative;
    font-family: "Roboto Condensed", "Arial Narrow", sans-serif;
    color: var(--body-ink);
    background: linear-gradient(180deg, var(--sky) 0%, var(--mint) 40%, var(--cream) 75%, var(--butter) 100%);
  }
  .brand {
    position: absolute; top: 118px; left: 0; width: 854px;
    text-align: center;
    font-family: "Roboto", Arial, sans-serif;
    font-weight: 700; font-size: 30px; color: var(--brand-blue);
  }
  .title-banner { position: absolute; left: 258px; top: 190px; width: 330px; height: 66px; }
  .title-banner svg { position: absolute; inset: 0; }
  .title-banner h1 {
    position: relative; text-align: center; line-height: 66px;
    font-family: "Roboto", Arial, sans-serif; font-weight: 700;
    font-size: 30px; color: #fff;
  }
  .subtitle {
    position: absolute; left: 195px; top: 266px; width: 450px; height: 39px;
    background: var(--band);
    text-align: center; line-height: 39px;
    font-family: "Roboto", Arial, sans-serif; font-weight: 700;
    font-size: 25px; color: var(--navy);
  }
  .section { position: absolute; left: 45px; width: 540px; }
  .section h2 {
    font-family: "Roboto", Arial, sans-serif; font-weight: 700;
    font-size: 20px; color: var(--orange); letter-spacing: 0.3px;
    margin-bottom: 12px;
  }
  .section ul { list-style: none; padding-left: 10px; }
  .section li {
    font-size: 12.5px; line-height: 22.4px; position: relative; padding-left: 9px;
  }
  .section li::before { content: "-"; position: absolute; left: 0; }
  .reasons { top: 352px; width: 595px; }
  .reversal { top: 586px; }
  .care { top: 766px; }
  .photo { position: absolute; }
  .photo-hairbrush { left: 605px; top: 381px; width: 203px; height: 144px;
    background: linear-gradient(135deg, #f2f2f2, #d9b8a4 55%, #b55a34); }
  .photo-food { left: 600px; top: 608px; width: 206px; height: 137px;
    background: linear-gradient(135deg, #8a6a48, #c9a26e 45%, #6f9a3c 80%, #9a6b45); }
  .photo-oil { left: 600px; top: 809px; width: 207px; height: 149px;
    background: linear-gradient(90deg, #e7e4a8 0%, #f6f6f0 35%, #5a4a44 70%, #2a211f 100%); }
  .closing {
    position: absolute; left: 45px; top: 1013px; width: 760px;
    font-family: "Roboto Condensed", "Arial Narrow", sans-serif; font-weight: 500;
    font-size: 14.5px; line-height: 19px; color: var(--green); text-transform: uppercase;
  }
  .explore {
    position: absolute; left: 30px; top: 1072px; width: 330px; text-align: center;
    font-family: "Roboto Condensed", "Arial Narrow", sans-serif; font-weight: 700;
    font-size: 29px; line-height: 38px; color: var(--ink);
  }
  .available {
    position: absolute; left: 560px; top: 1066px; width: 170px; text-align: center;
    font-family: "Roboto", Arial, sans-serif; font-weight: 700;
    font-size: 20px; color: var(--ink);
  }
  .store-badge {
    position: absolute; top: 1104px; width: 164px; height: 38px;
    background: #000; border: 1.5px solid #a6a6a6; border-radius: 7px;
  }
  .store-android { left: 462px; }
  .store-ios { left: 642px; }
</style>
</head>
<body>
  <div class="brand">Vitanest</div>

  <div class="title-banner">
    <svg width="330" height="66" viewBox="0 0 330 66" aria-hidden="true">
      <polygon points="20,6 330,0 312,60 6,66" fill="var(--accent-blue)"/>
      <polygon points="18,8 318,4 300,62 0,66" fill="var(--orange)"/>
    </svg>
    <h1>Heal Your Hair</h1>
  </div>

  <div class="subtitle">Keep Your Hair On &amp; Read On</div>

  <section class="section reasons">
    <h2>REASONS FOR HAIR FALL :</h2>
    <ul>
      <li>Excess hairfall can mean that the body does not have enough reserves to address the needs of the hair.</li>
      <li>Underlying medical conditions like PCOD, thyroid problems and hormonal imbalances.</li>
      <li>Stress and no time for rest can cause premature greying and thinning of hair.</li>
      <li>A diet high in processed foods, sugar, refined grains, oils and animal products.</li>
      <li>Hard water &amp; harsh chemicals in shampoos damage the hair shaft and follicle.</li>
      <li>Pollutants in air settle on the hair making it grimy, brittle and cause toxicity.</li>
      <li>Over treatment of hair with hair colourants, application of heat, tight braids and hair styling products damage the hair resulting in hairfall.</li>
    </ul>
  </section>
  <div class="photo photo-hairbrush" role="img" aria-label="Photo of a woman holding a hairbrush, looking at fallen hair"></div>

  <section class="section reversal">
    <h2>HOW CAN HAIR FALL BE RESERVED ?</h2>
    <ul>
      <li>Water rich fruits and vegetables in raw form, sprouts, nuts &amp; seeds nourish the cells of the hair.</li>
      <li>Exercise to improve blood circulation and aid in toxin removal.</li>
      <li>Outdoor time to soak in sunlight and fresh air.</li>
      <li>Get good quality sleep everyday and adopt stress management techniques.</li>
      <li>Repair and growth happens best in a relaxed state.</li>
    </ul>
  </section>
  <div class="photo photo-food" role="img" aria-label="Photo of fresh fruits, vegetables, fish and nuts on a wooden table"></div>

  <section class="section care">
    <h2>CARE OF HAIR :</h2>
    <ul>
      <li>Use a soft bristled brush to distribute natural oil uniformly, dislodge dandruff and dirt.</li>
      <li>Massage your hair with your fingertips to stimulate good blood circulation.</li>
      <li>Bathe in lukewarm or cold water. Avoid using hot water as it reduces hair oils.</li>
      <li>Use coconut milk, fruit purees or reetha. Normal water is fine too.</li>
      <li>Dry your hair in sunlight as opposed to a hair dryer.</li>
      <li>Buy hair products which has more natural ingredients than chemicals.</li>
      <li>Shoulder &amp; neck rotations improve circulation of nutrients to the hair follicles.</li>
    </ul>
  </section>
  <div class="photo photo-oil" role="img" aria-label="Photo of oil being poured from a glass bottle beside a woman with long glossy dark hair"></div>

  <p class="closing">It may take time to see results. The hairfall you see today is the result of wrong lifestyle.<br>Be patient and you will experience improvements in your crowning glory.</p>

  <div class="explore">To Explore More<br>Visit - www.vitanest.com</div>

  <div class="available">AVAILABLE ON</div>
  <div class="store-badge store-android" role="img" aria-label="App store download badge"></div>
  <div class="store-badge store-ios" role="img" aria-label="App store download badge"></div>
</body>
</html>
```